Baby Girl Maud Birth Announcement for Dec 1st 2020

Using an existing photo from an artist, build a 2 sided card with messaging and details on opposite side.

Style: fun, timeless, elegant, vibrant
Side 1:
Text "Welcome Maud".
Use file called FRONT BACKGROUND - Welcome Maud.
Consider 2 fonts, consider 2 colors of words. use provided image and monochromatic image of a heart
Side 2 content to be fit:
"Welcome to our little ray of light!"
"Maud Iris Jane Pelham"
Date of birth ---/--/----
Time of birth
Weight
Length
"Loving and Proud Parents : Clara Pelham - Ter Horst & Gregor Pelham"
Amazing and Wonderful God Parents : "Lehuanani Kekoa & Bastien De Wulf" + "Mira Chen Holloway & Dustin Holloway "

Target Market(s)

Family and friends.
International audience (european/asian/american).
Urban, up market,

Requirements
Must have
• Use file called FRONT BACKGROUND - Welcome Maud on the front
Nice to have
• Consider 2 fonts, consider 2 colors of words. use provided image and monochromatic image of a heart

```html
<!DOCTYPE html>
<html lang="en">
<head>
<meta charset="utf-8">
<title>Welcome Maud – Birth Announcement</title>
<link rel="stylesheet" href="https://fonts.googleapis.com/css2?family=Great+Vibes&family=Libre+Baskerville:wght@400;700&family=Roboto+Condensed:wght@500&display=swap">
<style>
  :root {
    --lilac: #b48fd2;
    --ink: #1b1b1b;
    --paper: #ffffff;
    --backdrop: #ededed;
  }
  * { margin: 0; padding: 0; box-sizing: border-box; }
  html, body {
    width: 1200px;
    height: 585px;
    overflow: hidden;
    background: var(--backdrop);
  }
  .spread {
    position: relative;
    width: 1200px;
    height: 585px;
    display: flex;
    justify-content: center;
    align-items: center;
    gap: 24px;
  }
  .card {
    position: relative;
    width: 570px;
    height: 410px;
    background: var(--paper);
    overflow: hidden;
  }

  /* Front side */
  .card-front__photo {
    position: absolute;
    inset: 0;
    background:
      radial-gradient(circle at 78% 42%, rgba(255,246,200,0.95) 0, rgba(255,230,150,0.6) 18%, rgba(255,230,150,0) 40%),
      radial-gradient(ellipse at 10% 85%, rgba(90,185,230,0.9) 0, rgba(90,185,230,0) 45%),
      radial-gradient(ellipse at 40% 30%, rgba(120,170,40,0.9) 0, rgba(120,170,40,0) 55%),
      radial-gradient(ellipse at 25% 65%, rgba(210,150,70,0.7) 0, rgba(210,150,70,0) 35%),
      linear-gradient(180deg, #8ab83a 0%, #c9d98a 45%, #e9eef0 75%, #f6f8f9 100%);
  }
  .card-front__overlay {
    position: absolute;
    inset: 0;
  }
  .card-front__welcome {
    position: absolute;
    left: 190px;
    top: 8px;
    font-family: "Great Vibes", cursive;
    font-size: 76px;
    color: var(--lilac);
    line-height: 1;
  }
  .card-front__name {
    position: absolute;
    left: 196px;
    top: 118px;
    font-family: "Libre Baskerville", serif;
    font-weight: 700;
    font-size: 58px;
    letter-spacing: 6px;
    color: var(--ink);
    line-height: 1;
  }

  /* Back side */
  .card-back {
    display: flex;
    flex-direction: column;
    align-items: center;
    text-align: center;
    padding-top: 44px;
  }
  .card-back__greeting {
    font-family: "Libre Baskerville", serif;
    font-weight: 700;
    font-size: 13.5px;
    letter-spacing: 2.4px;
    text-transform: uppercase;
    color: var(--ink);
  }
  .card-back__full-name {
    font-family: "Great Vibes", cursive;
    font-size: 52px;
    color: var(--lilac);
    line-height: 1.1;
    margin-top: 2px;
  }
  .card-back__stats {
    list-style: none;
    margin-top: 28px;
    font-family: "Roboto Condensed", sans-serif;
    font-weight: 500;
    font-size: 15px;
    letter-spacing: 1.8px;
    text-transform: uppercase;
    color: var(--ink);
    line-height: 24px;
  }
  .card-back__group { margin-top: 28px; }
  .card-back__group + .card-back__group { margin-top: 20px; }
  .card-back__label {
    font-family: "Libre Baskerville", serif;
    font-weight: 700;
    font-size: 13.5px;
    color: var(--lilac);
    line-height: 20px;
  }
  .card-back__people {
    font-family: "Libre Baskerville", serif;
    font-size: 14px;
    color: var(--ink);
    line-height: 20px;
  }
</style>
</head>
<body>
<main class="spread">
  <section class="card card-front" aria-label="Front of card">
    <div class="card-front__photo" role="img" aria-label="Bright sunlit photo of toy figures in a unicorn costume with small animals on a snowy ground, soft green and blue bokeh"></div>
    <svg class="card-front__overlay" viewBox="0 0 570 410" width="570" height="410" aria-hidden="true">
      <path d="M0,0 H570 V28 C470,30 400,34 350,48 C320,58 300,70 190,100 C140,108 80,112 0,112 Z" fill="#ffffff"/>
      <path d="M0,112 C80,112 140,108 190,100 C300,70 320,58 350,48 C400,34 470,30 570,28" fill="none" stroke="var(--lilac)" stroke-width="1.6"/>
      <path d="M428,118 C418,106 412,98 416,92 C420,86 427,88 429,94 C432,88 440,86 442,93 C444,100 436,108 428,118 Z" fill="none" stroke="var(--lilac)" stroke-width="2"/>
    </svg>
    <div class="card-front__welcome">welcome</div>
    <div class="card-front__name">MAUD</div>
  </section>

  <section class="card card-back" aria-label="Back of card">
    <h1 class="card-back__greeting">Welcome to our little ray of light!</h1>
    <h2 class="card-back__full-name">Maud Iris Jane Pelham</h2>
    <ul class="card-back__stats">
      <li>Oct. 1, 2020 at 6:02 AM</li>
      <li>7 Pounds, 2 Ounces</li>
      <li>19 Inches</li>
    </ul>
    <div class="card-back__group">
      <p class="card-back__label">Loving And Proud Parents:</p>
      <p class="card-back__people">Clara Pelham - Ter Horst &amp; Gregor Pelham</p>
    </div>
    <div class="card-back__group">
      <p class="card-back__label">Amazing and Wonderful God Parents:</p>
      <p class="card-back__people">Lehuanani Kekoa &amp; Bastien De Wulf</p>
      <p class="card-back__people">+ Mira Chen Holloway &amp; Dustin Holloway</p>
    </div>
  </section>
</main>
</body>
</html>
```